Business Card Design - Corporate

Create a sleek elegant business card layout while suggesting a color scheme. Convey cutting edge technology while maintaining a corporate feel that is easily readable.

Company designs and manufactures consumer electronic products for mass retail that are mainly app driven.

(vector logo and die-line provided)

Target Market(s)

Corporate level, tech industry.

Industry/Entity Type

Business

Contact Information for Business Card

Generic Info:

Name
Title
email
address
phone 1
phone 2
website (quelvane.com) on back

Font styles to use
Sans Serif

Requirements
Must have
• At least 2 colors + white on one side.
Nice to have
• Solid suggestion on color for logo and overall design. Color flood on back of card.
Should not have
• background texture like... marble, stone, patterns or circuit boards

```html
<!DOCTYPE html>
<html lang="en">
<head>
<meta charset="utf-8">
<title>Quelvane Business Card</title>
<link href="https://fonts.googleapis.com/css2?family=Open+Sans:wght@400;600&family=Montserrat:wght@300;400&display=swap" rel="stylesheet">
<style>
  :root {
    --backdrop: #3d3632;
    --card: #0c0c0d;
    --card-edge: #1a1a1b;
    --accent: #1e7fce;
    --text-light: #e6e6e6;
    --text-muted: #c9c9c9;
    --silver: #d4d6d8;
  }
  * { margin: 0; padding: 0; box-sizing: border-box; }
  html, body {
    width: 1200px;
    height: 900px;
    overflow: hidden;
    background: var(--backdrop);
  }
  .canvas {
    position: relative;
    width: 1200px;
    height: 900px;
    display: flex;
    align-items: center;
    justify-content: center;
    gap: 60px;
  }
  .card {
    position: relative;
    width: 525px;
    height: 300px;
    background: var(--card);
    border: 1px solid var(--card-edge);
    box-shadow: 0 12px 30px rgba(0,0,0,0.45);
    font-family: "Open Sans", sans-serif;
  }

  /* Front */
  .brand-mark {
    position: absolute;
    left: 38px;
    top: 50%;
    transform: translateY(-50%);
    display: flex;
    align-items: center;
    gap: 10px;
  }
  .brand-mark .dot {
    width: 22px;
    height: 22px;
    border-radius: 50%;
    background: var(--accent);
  }
  .brand-mark .name {
    font-family: "Open Sans", sans-serif;
    font-weight: 600;
    font-size: 22px;
    letter-spacing: 1px;
    color: var(--accent);
  }
  .divider {
    position: absolute;
    left: 232px;
    top: 62px;
    width: 1px;
    height: 176px;
    background: linear-gradient(to bottom, rgba(30,127,206,0), var(--accent) 40%, rgba(30,127,206,0));
  }
  .contact {
    position: absolute;
    left: 252px;
    top: 58px;
    color: var(--text-light);
  }
  .person-name {
    font-size: 19px;
    font-weight: 400;
    color: var(--accent);
    text-transform: uppercase;
    letter-spacing: 0.3px;
    line-height: 1.1;
  }
  .person-title {
    font-size: 13px;
    color: var(--text-muted);
    margin-bottom: 18px;
  }
  .contact-line {
    display: flex;
    align-items: center;
    gap: 8px;
    font-size: 13.5px;
    line-height: 19px;
  }
  .contact-line svg { width: 10px; height: 10px; fill: var(--accent); flex: none; }
  .address {
    margin-top: 14px;
    font-size: 13.5px;
    line-height: 19px;
  }

  /* Back */
  .card-back {
    display: flex;
    flex-direction: column;
    align-items: center;
    justify-content: center;
  }
  .wordmark {
    font-family: "Montserrat", sans-serif;
    font-weight: 300;
    font-size: 46px;
    letter-spacing: 8px;
    color: var(--silver);
  }
  .website {
    margin-top: 26px;
    margin-left: 150px;
    font-size: 13px;
    color: var(--text-light);
  }
</style>
</head>
<body>
<main class="canvas">
  <section class="card card-front">
    <div class="brand-mark">
      <span class="dot"></span>
      <span class="name">QUELVANE</span>
    </div>
    <div class="divider"></div>
    <div class="contact">
      <p class="person-name">Marcus Ellery</p>
      <p class="person-title">Managing Director</p>
      <p class="contact-line">
        <svg viewBox="0 0 10 10"><path d="M2 0.5 L3.6 2.6 L2.7 3.6 Q3.8 6 6.4 7.3 L7.4 6.4 L9.5 8 L8.4 9.5 Q2.5 8.5 0.5 1.6 Z"/></svg>
        (044)387215064
      </p>
      <p class="contact-line">
        <svg viewBox="0 0 10 10"><path d="M2 0.5 L3.6 2.6 L2.7 3.6 Q3.8 6 6.4 7.3 L7.4 6.4 L9.5 8 L8.4 9.5 Q2.5 8.5 0.5 1.6 Z"/></svg>
        (044)387215071
      </p>
      <p class="contact-line">
        <svg viewBox="0 0 10 10"><path d="M0 2 H10 V8.5 H0 Z M0.6 2.5 L5 5.6 L9.4 2.5" stroke="#0c0c0d" stroke-width="0.8"/></svg>
        hello@quelvane.com
      </p>
      <p class="address">18 Marlow Park Avenue,<br>Northgate 60412</p>
    </div>
  </section>

  <section class="card card-back">
    <p class="wordmark">QUELVANE</p>
    <p class="website">www.quelvane.com</p>
  </section>
</main>
</body>
</html>
```